QR TILL WORKS , CREDIT CARD PROCESSING EQUIPMENT

qrtillworks is a sub division of Tallow a credit car processing co.
morgan tessler
14 cedar hollow ln
Larkfield EX 07312
suite 412

qrtillworks.example
cell 555-214-7730
office 555-861-2093
we sell pos systems to merchant who want to accept credit cards at there retail location.
black card would be nice buit open to different ideas

Target Market(s)

retail merchants

Industry/Entity Type

credit card processing

Contact Information for Business Card

card should include web site phone address

Colors

Designer to choose colors to be used in the design.

Requirements
Should not have
• red

```html
<!DOCTYPE html>
<html lang="en">
<head>
<meta charset="utf-8">
<title>QR Till Works — Business Card</title>
<link rel="stylesheet" href="https://fonts.googleapis.com/css2?family=Montserrat:wght@500;600;700&display=swap">
<style>
  :root {
    --page: #e9e6e1;
    --card-dark: #302d2d;
    --card-grey: #656567;
    --accent-yellow: #e2c32f;
    --text-light: #ffffff;
    --text-soft: #f1f1f1;
    --text-on-grey: #3a3838;
  }
  * { margin: 0; padding: 0; box-sizing: border-box; }
  html, body {
    width: 1200px; height: 1200px; overflow: hidden;
    background: var(--page);
    font-family: "Montserrat", sans-serif;
  }
  .sheet { position: relative; width: 1200px; height: 1200px; }
  .card {
    position: absolute; left: 200px; width: 800px; height: 454px;
    background: var(--card-dark); overflow: hidden;
    box-shadow: 0 6px 18px rgba(0,0,0,0.18);
  }
  .card--front { top: 110px; }
  .card--back { top: 636px; }
  .card-shapes { position: absolute; inset: 0; width: 800px; height: 454px; }

  .holder-name {
    position: absolute; left: 84px; top: 22px; height: 94px;
    display: flex; align-items: center;
    color: var(--text-light); font-weight: 700; font-size: 35px; letter-spacing: 3px;
  }
  .brand-name {
    position: absolute; color: var(--text-light); font-weight: 600; line-height: 1.02;
    white-space: nowrap;
  }
  .card--front .brand-name { left: 52px; top: 240px; font-size: 40px; }
  .card--back .brand-name { left: 290px; top: 158px; font-size: 74px; }

  .contact-line {
    position: absolute; left: 472px;
    color: var(--text-soft); font-weight: 500; font-size: 21px;
    letter-spacing: 2px; line-height: 26px; white-space: nowrap;
  }
  .contact-line--address { top: 140px; }
  .contact-line--phone { top: 258px; }
  .contact-line--web { top: 380px; }

  .site-vertical {
    position: absolute; left: 60px; top: 50px;
    writing-mode: vertical-rl;
    color: var(--text-on-grey); font-weight: 500; font-size: 30px; letter-spacing: 3px;
  }
</style>
</head>
<body>
<main class="sheet">

  <section class="card card--front" aria-label="Card front">
    <svg class="card-shapes" viewBox="0 0 800 454" aria-hidden="true">
      <rect x="0" y="22" width="800" height="94" fill="var(--card-grey)"/>
      <polygon points="286,130 382,130 402,224 306,224" fill="var(--accent-yellow)"/>
      <polygon points="394,130 800,130 800,224 414,224" fill="var(--card-grey)"/>
      <polygon points="306,237 400,237 420,331 326,331" fill="var(--accent-yellow)"/>
      <polygon points="414,237 800,237 800,331 434,331" fill="var(--card-grey)"/>
      <polygon points="328,346 420,346 440,440 348,440" fill="var(--accent-yellow)"/>
      <polygon points="434,346 800,346 800,440 454,440" fill="var(--card-grey)"/>
      <g transform="translate(344 177)" fill="var(--card-dark)">
        <path d="M0,-24 C-13,-24 -20,-14 -20,-4 C-20,8 -6,18 0,32 C6,18 20,8 20,-4 C20,-14 13,-24 0,-24 Z"/>
        <circle cx="0" cy="-4" r="7" fill="var(--accent-yellow)"/>
      </g>
      <g transform="translate(363 284)" fill="var(--card-dark)">
        <path d="M-20,-22 L-11,-24 L-4,-10 L-10,-5 C-7,4 0,11 8,15 L13,9 L25,16 L23,25 C20,27 14,28 8,25 C-6,19 -18,7 -23,-7 C-25,-13 -24,-18 -20,-22 Z"/>
      </g>
      <g transform="translate(384 393)" fill="none" stroke="var(--card-dark)" stroke-width="4">
        <circle r="26"/>
        <ellipse rx="11" ry="26"/>
        <line x1="0" y1="-26" x2="0" y2="26"/>
        <line x1="-26" y1="0" x2="26" y2="0"/>
        <line x1="-22" y1="-13" x2="22" y2="-13"/>
        <line x1="-22" y1="13" x2="22" y2="13"/>
      </g>
    </svg>
    <h1 class="holder-name">MORGAN TESSLER</h1>
    <p class="brand-name">QR Till<br>Works</p>
    <p class="contact-line contact-line--address">14 Cedar Hollow ln<br>Larkfield EX 07312<br>Suite 412</p>
    <p class="contact-line contact-line--phone">555-214-7730<br>555-861-2093</p>
    <p class="contact-line contact-line--web">qrtillworks.example</p>
  </section>

  <section class="card card--back" aria-label="Card back">
    <svg class="card-shapes" viewBox="0 0 800 454" aria-hidden="true">
      <polygon points="0,0 155,0 204,454 0,454" fill="var(--card-grey)"/>
    </svg>
    <p class="site-vertical">qrtillworks.example</p>
    <p class="brand-name">QR Till<br>Works</p>
  </section>

</main>
</body>
</html>
```